Consulting/ Manufacturers Representative Website

I need a website for a consulting/manufacturer representative company in Texas called Heron Works Advisors. We Uncover and implement the right solution, at the right time, in the right way. We consult, we train, we offer project management, we offer performance improvement, we offer value creation, we turn stagnation into growth, and we offer corporate performance improvement.
I want the design to load on desktop and mobile, I want the site to look and feel professional like a large firm, and I want the site to be a marketing tool and establish a strong online presence.

Target Market(s)

City Governments, State Governments, County Governments, US Government, Power Plants, Refineries, Chemical Plants, Industrial customers

Industry/Entity Type

Consulting

Number of Pages Required

5+ page

Requirements
Must have
• mobile and desktop compatible, professional look, must be a fast website, company email and contact capabilities, contact page, company logo on website, SEO optimized, must display different industries served: Energy, Public (Government, Not For Profit, Educational), Transportation & Logistics, Business Services.
• Show that I help customers operate in a cleaner, safer and more economical way.
Nice to have
• news letter, news feed, show that company is principles based.
Should not have
• slow site, cheap look

```html
<!DOCTYPE html>
<html lang="en">
<head>
<meta charset="utf-8">
<title>Heron Works Advisors</title>
<link rel="stylesheet" href="https://fonts.googleapis.com/css2?family=Montserrat:wght@400;600;700;800&family=Open+Sans:ital,wght@0,400;0,600;0,700;1,400&display=swap">
<style>
:root{
  --ink:#111111;
  --text:#333333;
  --muted:#666666;
  --white:#ffffff;
  --paper:#f4f4f4;
  --line:#dddddd;
  --ghost:#ececec;
  --footer:#0d0d0d;
  --footer-base:#050505;
  --night-1:#0c1a3a;
  --night-2:#1b2f5c;
  --night-3:#0a0f1c;
}
*{box-sizing:border-box;margin:0;padding:0}
html,body{width:1200px;height:2655px;overflow:hidden}
body{font-family:"Open Sans",Arial,sans-serif;color:var(--text);background:var(--white);font-size:12px}
.wrap{width:878px;margin:0 auto;position:relative}
h1,h2,h3,h4{font-family:"Montserrat",Arial,sans-serif}

/* hero */
.hero{position:relative;height:499px;background:linear-gradient(180deg,var(--night-1) 0%,var(--night-2) 45%,#273a55 70%,var(--night-3) 100%);color:var(--white);overflow:hidden}
.hero-photo{position:absolute;inset:0;background:radial-gradient(ellipse at 40% 55%,rgba(200,210,220,.35) 0%,rgba(0,0,0,0) 45%),linear-gradient(180deg,rgba(0,0,0,.1),rgba(0,0,0,.45))}
.topbar{position:absolute;left:161px;top:0;width:878px;height:88px}
.brand{position:absolute;left:6px;top:10px;width:62px;display:flex;flex-direction:column;align-items:center;gap:4px;font-family:"Montserrat",sans-serif;font-weight:700;font-size:7.5px;line-height:1.2;letter-spacing:.3px;text-align:center;color:var(--white)}
.brand-mark{width:14px;height:14px;border:1.5px solid var(--white)}
.contact-strip{position:absolute;left:92px;top:14px;display:flex;gap:24px;font-size:11px;align-items:center}
.contact-strip span{display:flex;align-items:center;gap:7px}
.social{position:absolute;right:0;top:12px;display:flex;gap:6px}
.social i,.footer-social i{display:block;width:16px;height:16px;border:1.5px solid var(--white);border-radius:50%}
.nav{position:absolute;left:80px;right:0;top:44px;height:44px;border-top:1px solid rgba(255,255,255,.35);display:flex}
.nav a{display:flex;align-items:center;padding:0 22px;font-size:10px;font-weight:600;color:var(--white);text-decoration:none;border-right:1px solid rgba(255,255,255,.35)}
.nav a:first-child{border-left:1px solid rgba(255,255,255,.35);background:rgba(255,255,255,.08)}
.hero-copy{position:absolute;left:0;right:0;top:214px;text-align:center}
.hero-copy h1{font-size:29px;font-weight:700;letter-spacing:.5px}
.hero-copy p{width:520px;margin:14px auto 0;font-size:11px;line-height:20px}
.btn-outline{display:inline-flex;align-items:center;gap:8px;margin-top:24px;height:38px;padding:0 22px;border:1.5px solid var(--white);border-radius:19px;font-size:10px;font-weight:700;font-family:"Montserrat",sans-serif;color:var(--white)}
.slide-arrow{position:absolute;top:236px}
.slide-arrow.prev{left:64px}.slide-arrow.next{right:42px}
.dots{position:absolute;left:0;right:0;top:459px;display:flex;justify-content:center;gap:4px}
.dots i{width:10px;height:10px;border:1px solid var(--white);border-radius:50%}
.dots i.on{background:var(--white)}

/* section heading */
.sec-head{position:relative;height:60px}
.sec-head .ghost{position:absolute;left:0;top:0;font-family:"Montserrat",sans-serif;font-weight:800;font-size:46px;color:var(--ghost);letter-spacing:1px;line-height:1}
.sec-head h2{position:absolute;top:14px;font-size:14px;font-weight:700;color:var(--ink)}
.sec-head h2::after{content:"";position:absolute;left:0;top:30px;width:38px;height:2px;background:var(--ink)}
.pager{position:absolute;right:0;top:16px;display:flex;gap:18px}

/* about */
.about{position:relative;height:395px}
.about .wrap{padding-top:42px}
.about-text{width:565px}
.about-text .sec-head h2{left:179px}
.about-text p.lead{margin-top:6px;font-size:10px;line-height:20px;color:var(--text)}
.ticks{list-style:none;margin-top:16px}
.ticks li{display:flex;align-items:center;gap:12px;height:23px;margin-left:30px;font-size:10px}
.btn-solid{display:inline-flex;align-items:center;justify-content:center;margin-top:24px;width:150px;height:39px;border-radius:20px;background:var(--ink);color:var(--white);font-family:"Montserrat",sans-serif;font-weight:700;font-size:10px}
.about-photo{position:absolute;left:761px;top:0;width:439px;height:395px;background:linear-gradient(135deg,#1a2b4e 0%,#3c5a84 40%,#c89a7c 60%,#24344f 100%)}

/* insights */
.insights{margin-top:39px;height:442px;background:var(--paper)}
.insights .wrap{padding-top:40px}
.insights .sec-head h2{left:179px}
.insight-grid{display:flex;gap:22px;margin-top:27px}
.insight{position:relative;width:278px;height:242px;color:var(--white);overflow:hidden}
.insight .caption{position:absolute;left:21px;bottom:22px;right:16px;z-index:1}
.insight em{font-size:10px;display:block;margin-bottom:3px}
.insight h3{font-size:15.5px;line-height:20px;font-family:"Open Sans",sans-serif;font-weight:700}
.show-more{text-align:right;margin-top:20px;font-family:"Montserrat",sans-serif;font-weight:700;font-size:10px;color:var(--ink);text-decoration:underline}
.img-solar{background:linear-gradient(180deg,#3a7fd0 0%,#8ab8e8 40%,#2c4f86 62%,#6b8a3a 100%)}
.img-house{background:linear-gradient(180deg,#4b6f94 0%,#7f8c84 45%,#b7b0a2 65%,#566a3c 100%)}
.img-gas{background:linear-gradient(180deg,#0d1a33 0%,#2a3e5e 45%,#8a9aa8 65%,#0c1510 100%)}
.insight::after{content:"";position:absolute;inset:0;background:linear-gradient(180deg,rgba(0,0,0,0) 45%,rgba(0,0,0,.55) 100%)}

/* reviews */
.reviews{height:363px}
.reviews .wrap{padding-top:54px}
.reviews .sec-head h2{left:267px}
.review-grid{display:flex;gap:22px;margin-top:5px}
.review{width:428px;height:195px;border:1px solid var(--line);background:var(--white);padding:34px 34px 0 32px;position:relative}
.review blockquote{position:relative;padding-left:24px;font-style:italic;font-size:10px;line-height:19px;color:var(--text)}
.review blockquote::before{content:"\201C";position:absolute;left:0;top:-8px;font-size:34px;color:#b5b5b5;font-family:Georgia,serif;font-style:normal}
.review blockquote::after{content:"\201D";font-size:30px;color:#b5b5b5;font-family:Georgia,serif;font-style:normal;line-height:0;vertical-align:-12px;margin-left:4px}
.reviewer{display:flex;align-items:center;gap:20px;margin-top:20px;padding-left:24px}
.avatar{width:52px;height:52px;background:#d9d9d9}
.reviewer h4{font-size:14px;font-weight:700;color:var(--ink)}
.reviewer span{font-size:10px;font-style:italic;color:var(--muted)}

/* news */
.news{height:551px;background:var(--paper)}
.news .wrap{padding-top:51px}
.news .sec-head h2{left:88px}
.news-grid{display:flex;gap:22px;margin-top:14px}
.news-card{width:278px;height:369px;background:var(--white)}
.news-img{position:relative;height:186px}
.news-date{position:absolute;left:0;bottom:-8px;background:var(--ink);color:var(--white);font-size:8.5px;padding:0 13px;height:22px;display:flex;align-items:center}
.img-hands{background:linear-gradient(135deg,#1a2b4e 0%,#3c5a84 45%,#c89a7c 60%,#24344f 100%)}
.news-body{padding:31px 16px 0 16px}
.news-body h3{font-size:15px;font-family:"Open Sans",sans-serif;font-weight:700;color:var(--ink)}
.news-body p{margin-top:14px;font-size:10px;line-height:19px}
.news-body .more{display:flex;align-items:center;gap:7px;margin-top:16px;font-size:10px;font-weight:700;color:var(--ink)}

/* footer */
.footer{height:317px;background:var(--footer);color:var(--white)}
.footer .wrap{display:flex;justify-content:space-between;padding-top:66px}
.foot-col{width:262px}
.foot-col h4{font-size:14px;font-weight:700;margin-bottom:15px}
.foot-col p{font-size:10px;line-height:19px}
.foot-list{list-style:none;margin-top:18px}
.foot-list li{display:flex;align-items:center;gap:12px;font-size:10px;height:27px}
.foot-mid{width:300px;text-align:center;padding-top:4px}
.foot-brand{display:inline-flex;flex-direction:column;align-items:center;gap:8px;font-family:"Montserrat",sans-serif;font-weight:700;font-size:15px;letter-spacing:1px}
.foot-brand i{width:26px;height:26px;border:2px solid var(--white);border-radius:50%}
.foot-mid p{margin-top:17px;font-size:10px;line-height:19px}
.footer-social{display:flex;gap:6px;justify-content:center;margin-top:14px}
.footer-social i{width:22px;height:22px}
.newsletter{margin-top:24px;display:flex;height:42px;width:228px;border-radius:21px;overflow:hidden;background:var(--white)}
.newsletter span{flex:1;display:flex;align-items:center;padding-left:18px;font-size:9px;font-style:italic;color:#999}
.newsletter b{width:54px;background:#9a9a9a;display:flex;align-items:center;justify-content:center}
.base{height:49px;background:var(--footer-base);color:#aaa;font-size:8.5px}
.base .wrap{display:flex;justify-content:space-between;align-items:center;height:49px}
.base nav{display:flex;gap:20px}
</style>
</head>
<body>

<header class="hero">
  <div class="hero-photo" role="img" aria-label="Liquefied natural gas plant with a storage sphere lit up at night"></div>
  <div class="topbar">
    <div class="brand"><span class="brand-mark"></span><span>HERON WORKS<br>ADVISORS</span></div>
    <div class="contact-strip">
      <span><svg width="12" height="9" viewBox="0 0 12 9"><rect x=".5" y=".5" width="11" height="8" fill="none" stroke="#fff"/><path d="M.5 .5 6 5l5.5-4.5" fill="none" stroke="#fff"/></svg>info@heronworks.com</span>
      <span><svg width="11" height="11" viewBox="0 0 11 11"><path d="M2 1l2 2-1 1.5c.8 1.5 2 2.7 3.5 3.5L8 7l2 2-1.5 1.5C4.5 10 1 6.5.5 2.5z" fill="none" stroke="#fff"/></svg>+1 (555) 0142 - 7788</span>
    </div>
    <div class="social"><i></i><i></i><i></i><i></i></div>
    <nav class="nav"><a>HOME</a><a>ABOUT US</a><a>SERVICES</a><a>BLOG</a><a>CONTACT US</a></nav>
  </div>
  <svg class="slide-arrow prev" width="40" height="36" viewBox="0 0 40 36"><path d="M20 2 38 34H2z" fill="none" stroke="#fff" stroke-width="1.2"/><path d="M22 18l-4 4 4 4" fill="none" stroke="#fff" stroke-width="1.2" transform="translate(0,-4)"/></svg>
  <svg class="slide-arrow next" width="40" height="36" viewBox="0 0 40 36"><path d="M20 2 38 34H2z" fill="none" stroke="#fff" stroke-width="1.2"/><path d="M18 14l4 4-4 4" fill="none" stroke="#fff" stroke-width="1.2"/></svg>
  <div class="hero-copy">
    <h1>LIQUEFIED NATURAL GAS PLANT</h1>
    <p>Lorem ipsum dolor sit amet, consectetur adipiscing elit. Phasellus mollis nunc a justo interdum efficitur. Donec hendrerit eros sit amet finibus bibendum. Maecenas sit amet orci sem.</p>
    <span class="btn-outline">GET A QUOTE <svg width="6" height="9" viewBox="0 0 6 9"><path d="M1 1l3.5 3.5L1 8" fill="none" stroke="#fff" stroke-width="1.4"/></svg></span>
  </div>
  <div class="dots"><i class="on"></i><i></i><i></i></div>
</header>

<section class="about">
  <div class="wrap">
    <div class="about-text">
      <div class="sec-head"><span class="ghost">ABOUT</span><h2>WHO WE ARE</h2></div>
      <p class="lead">Lorem ipsum dolor sit amet, consectetur adipiscing elit. Phasellus mollis nunc a justo interdum efficitur. Donec hendrerit eros sit amet finibus bibendum. Maecenas sit amet orci sem. Proin efficitur justo sodales fermentum pellentesque. Sed blandit tempor libero, a convallis sapien luctus eu. Donec sagittis semper elit, accumsan fermentum.</p>
      <ul class="ticks">
        <li><svg width="11" height="9" viewBox="0 0 11 9"><path d="M1 4.5 4 7.5 10 1" fill="none" stroke="#111" stroke-width="2"/></svg>We Uncover and implement the right solution, at the right time, in the right way. We consult, we train.</li>
        <li><svg width="11" height="9" viewBox="0 0 11 9"><path d="M1 4.5 4 7.5 10 1" fill="none" stroke="#111" stroke-width="2"/></svg>We offer project management</li>
        <li><svg width="11" height="9" viewBox="0 0 11 9"><path d="M1 4.5 4 7.5 10 1" fill="none" stroke="#111" stroke-width="2"/></svg>We offer performance improvement</li>
        <li><svg width="11" height="9" viewBox="0 0 11 9"><path d="M1 4.5 4 7.5 10 1" fill="none" stroke="#111" stroke-width="2"/></svg>We offer value creation</li>
        <li><svg width="11" height="9" viewBox="0 0 11 9"><path d="M1 4.5 4 7.5 10 1" fill="none" stroke="#111" stroke-width="2"/></svg>We turn stagnation into growth</li>
        <li><svg width="11" height="9" viewBox="0 0 11 9"><path d="M1 4.5 4 7.5 10 1" fill="none" stroke="#111" stroke-width="2"/></svg>We offer corporate performance improvement</li>
      </ul>
      <span class="btn-solid">READ MORE</span>
    </div>
  </div>
  <div class="about-photo" role="img" aria-label="Business handshake in front of a night city skyline"></div>
</section>

<section class="insights">
  <div class="wrap">
    <div class="sec-head"><span class="ghost">SERVICES</span><h2>LATEST INSIGHTS</h2>
      <div class="pager">
        <svg width="26" height="10" viewBox="0 0 26 10"><path d="M25 5H2M6 1 2 5l4 4" fill="none" stroke="#111" stroke-width="1.6"/></svg>
        <svg width="26" height="10" viewBox="0 0 26 10"><path d="M1 5h23M20 1l4 4-4 4" fill="none" stroke="#111" stroke-width="1.6"/></svg>
      </div>
    </div>
    <div class="insight-grid">
      <article class="insight img-solar" role="img" aria-label="Solar panels in a field under blue sky">
        <div class="caption"><em>Industrial Solar</em><h3>Lorem ipsum dolor sit amet, consectetur adipiscing elit. &#x2192;</h3></div>
      </article>
      <article class="insight img-house" role="img" aria-label="Historic two-storey house with a veranda">
        <div class="caption"><em>City Vista of Houston</em><h3>Lorem ipsum dolor sit amet, consectetur adipiscing elit. &#x2192;</h3></div>
      </article>
      <article class="insight img-gas" role="img" aria-label="Gas storage spheres lit at night">
        <div class="caption"><em>Liquefied Natural Gas Plant</em><h3>Lorem ipsum dolor sit amet, consectetur adipiscing elit. &#x2192;</h3></div>
      </article>
    </div>
    <div class="show-more">SHOW MORE</div>
  </div>
</section>

<section class="reviews">
  <div class="wrap">
    <div class="sec-head"><span class="ghost">TESTIMONIALS</span><h2>CLIENT REVIEWS</h2>
      <div class="pager">
        <svg width="26" height="10" viewBox="0 0 26 10"><path d="M25 5H2M6 1 2 5l4 4" fill="none" stroke="#111" stroke-width="1.6"/></svg>
        <svg width="26" height="10" viewBox="0 0 26 10"><path d="M1 5h23M20 1l4 4-4 4" fill="none" stroke="#111" stroke-width="1.6"/></svg>
      </div>
    </div>
    <div class="review-grid">
      <article class="review">
        <blockquote>Lorem ipsum dolor sit amet, consectetur adipiscing elit. Phasellus mollis nunc a justo interdum efficitur. Donec hendrerit eros sit amet finibus bibendum. Maecenas sit amet orci sem. Proin efficitur justo.</blockquote>
        <div class="reviewer"><div class="avatar" role="img" aria-label="Client avatar placeholder"></div><div><h4>DONEC SAGITTIS</h4><span>Client</span></div></div>
      </article>
      <article class="review">
        <blockquote>Lorem ipsum dolor sit amet, consectetur adipiscing elit. Phasellus mollis nunc a justo interdum efficitur. Donec hendrerit eros sit amet finibus bibendum. Maecenas sit amet orci sem. Proin efficitur justo.</blockquote>
        <div class="reviewer"><div class="avatar" role="img" aria-label="Client avatar placeholder"></div><div><h4>DONEC SAGITTIS</h4><span>Client</span></div></div>
      </article>
    </div>
  </div>
</section>

<section class="news">
  <div class="wrap">
    <div class="sec-head"><span class="ghost">NEWS</span><h2>LATEST NEWS</h2></div>
    <div class="news-grid">
      <article class="news-card">
        <div class="news-img img-hands" role="img" aria-label="Business handshake over a city skyline"><span class="news-date">JUNE 27, 2018</span></div>
        <div class="news-body"><h3>Lorem ipsum dolor sit amet</h3><p>Phasellus mollis nunc a justo interdum efficitur. Donec hendrerit eros sit amet finibus bibendum. Maecenas sit amet orci sem.</p><span class="more">More <svg width="5" height="8" viewBox="0 0 5 8"><path d="M1 1l3 3-3 3" fill="none" stroke="#111" stroke-width="1.3"/></svg></span></div>
      </article>
      <article class="news-card">
        <div class="news-img img-solar" role="img" aria-label="Solar panels in a green field"><span class="news-date">JUNE 27, 2018</span></div>
        <div class="news-body"><h3>Lorem ipsum dolor sit amet</h3><p>Phasellus mollis nunc a justo interdum efficitur. Donec hendrerit eros sit amet finibus bibendum. Maecenas sit amet orci sem.</p><span class="more">More <svg width="5" height="8" viewBox="0 0 5 8"><path d="M1 1l3 3-3 3" fill="none" stroke="#111" stroke-width="1.3"/></svg></span></div>
      </article>
      <article class="news-card">
        <div class="news-img img-gas" role="img" aria-label="Gas storage sphere lit at night"><span class="news-date">JUNE 27, 2018</span></div>
        <div class="news-body"><h3>Lorem ipsum dolor sit amet</h3><p>Phasellus mollis nunc a justo interdum efficitur. Donec hendrerit eros sit amet finibus bibendum. Maecenas sit amet orci sem.</p><span class="more">More <svg width="5" height="8" viewBox="0 0 5 8"><path d="M1 1l3 3-3 3" fill="none" stroke="#111" stroke-width="1.3"/></svg></span></div>
      </article>
    </div>
  </div>
</section>

<footer class="footer">
  <div class="wrap">
    <div class="foot-col">
      <h4>CONTACT US</h4>
      <p>Lorem ipsum dolor sit amet, consectetur adipiscing elit. Phasellus mollis.</p>
      <ul class="foot-list">
        <li><svg width="9" height="12" viewBox="0 0 9 12"><path d="M4.5 11S1 6.5 1 4.5a3.5 3.5 0 0 1 7 0C8 6.5 4.5 11 4.5 11z" fill="none" stroke="#fff"/><circle cx="4.5" cy="4.5" r="1.2" fill="none" stroke="#fff"/></svg>123 Aenean facilisis, Consectetur.</li>
        <li><svg width="11" height="11" viewBox="0 0 11 11"><path d="M2 1l2 2-1 1.5c.8 1.5 2 2.7 3.5 3.5L8 7l2 2-1.5 1.5C4.5 10 1 6.5.5 2.5z" fill="none" stroke="#fff"/></svg>Phone: +1 (555) 0142 - 7788</li>
        <li><svg width="12" height="9" viewBox="0 0 12 9"><rect x=".5" y=".5" width="11" height="8" fill="none" stroke="#fff"/><path d="M.5 .5 6 5l5.5-4.5" fill="none" stroke="#fff"/></svg>E-Mail: info@heronworks.com</li>
      </ul>
    </div>
    <div class="foot-mid">
      <div class="foot-brand"><i></i><span>HERON WORKS ADVISORS</span></div>
      <p>Lorem ipsum dolor sit amet, consectetur adipiscing elit. Phasellus mollis nunc a justo interdum efficitur. Donec hendrerit eros sit amet finibus bibendum.</p>
      <div class="footer-social"><i></i><i></i><i></i><i></i></div>
    </div>
    <div class="foot-col" style="width:228px">
      <h4>NEWSLETTER</h4>
      <p>Lorem ipsum dolor sit amet, consectetur adipiscing elit. Phasellus mollis.</p>
      <div class="newsletter"><span>Enter your email address</span><b><svg width="6" height="9" viewBox="0 0 6 9"><path d="M1 1l3.5 3.5L1 8" fill="none" stroke="#fff" stroke-width="1.4"/></svg></b></div>
    </div>
  </div>
</footer>
<div class="base">
  <div class="wrap">
    <span>&copy; 2018 Heron Works Advisors - All Rights Reserved.</span>
    <nav><span>HOME</span><span>ABOUT US</span><span>SERVICES</span><span>BLOG</span><span>CONTACT US</span></nav>
  </div>
</div>

</body>
</html>
```